Podcast cover art (not a logo)

I’m launching an audio-only podcast for parents of neurodivergent children. The podcast is meant to feel like a calm, trusted professional voice — not a brand or a performance.

Style direction:
--Clean and minimal
--Calm and grounded
--Professional, not playful
--Nothing flashy, loud, or busy
--No cartoon imagery

Content on the cover:
--Podcast title: Under the Quiet Surface
--Subtitle or tagline: Supporting Neurodivergent Kids with Science, Not Shame (or Understanding Neurodivergent Kids)
--No episode numbers, no dates

Design preferences:
--Text-forward design
--Neutral or soft colors (muted blues, grays, off-whites)
--High contrast for readability at small sizes
--Simple, timeless font

What I do NOT want:
--A logo or branding system
--Illustrations of children or families
--Bright colors or playful graphics
--Trendy fonts or visual effects

Technical requirements:
--Square image
--3000 × 3000 pixels
--RGB color mode
--JPEG or PNG
--File size under 500 KB

Deliverables:
--Final cover art file
--Optional: one or two alternate background color versions

```html
<!DOCTYPE html>
<html lang="en">
<head>
<meta charset="utf-8">
<title>Under the Quiet Surface — Podcast Cover</title>
<link href="https://fonts.googleapis.com/css2?family=Montserrat:wght@400;900&display=swap" rel="stylesheet">
<style>
  :root {
    --page: #e9ebee;
    --cover: #ffffff;
    --texture-soft: #f4f5f6;
    --texture-deep: #dadcdf;
    --navy: #1d3a5c;
  }
  * { box-sizing: border-box; margin: 0; padding: 0; }
  html, body {
    width: 1200px; height: 590px; overflow: hidden;
    background: var(--page);
    font-family: "Montserrat", Arial, sans-serif;
  }
  .canvas {
    width: 1200px; height: 590px;
    display: flex; align-items: center; justify-content: center;
  }
  .cover {
    position: relative;
    width: 590px; height: 590px;
    background: var(--cover);
    overflow: hidden;
  }
  .cover-texture {
    position: absolute; inset: 0;
    background:
      radial-gradient(circle at 50% 45%, var(--cover) 0%, var(--cover) 38%, transparent 70%),
      linear-gradient(135deg, var(--texture-deep) 0%, var(--texture-soft) 35%, var(--texture-soft) 65%, var(--texture-deep) 100%);
  }
  .title {
    position: absolute; left: 0; right: 0; top: 112px;
    text-align: center;
    color: var(--navy);
    font-weight: 900;
    line-height: 1;
    letter-spacing: 1px;
  }
  .title-line { display: block; }
  .title-line--top { font-size: 70px; }
  .title-line--mid { font-size: 52px; margin-top: 6px; }
  .title-line--bottom { font-size: 72px; margin-top: 6px; }
  .tagline {
    position: absolute; left: 0; right: 0; top: 400px;
    text-align: center;
    color: var(--navy);
    font-weight: 400;
    font-size: 17px;
    letter-spacing: 2px;
    line-height: 1.6;
  }
</style>
</head>
<body>
  <main class="canvas">
    <section class="cover">
      <div class="cover-texture" role="img" aria-label="Soft grey background texture of fine radiating dotted lines"></div>

      <h1 class="title">
        <span class="title-line title-line--top">UNDER</span>
        <span class="title-line title-line--mid">THE QUIET</span>
        <span class="title-line title-line--bottom">SURFACE</span>
      </h1>

      <p class="tagline">UNDERSTANDING<br>NEURODIVERGENT KIDS</p>
    </section>
  </main>
</body>
</html>
```